Software company specialized in data analytics and professional services

We need a landing page design for our business. It should include our logo design. It should have multiple sections :
- stylish head
- what we do (data analytics software, professional services)
- contact form

Target Market(s)

Companies, B2B

Industry/Entity Type

Data

Number of Pages Required

1 page

Font styles to use
Sans Serif

Requirements
Must have
• Dark theme
Should not have
• Gradients on buttons

```html
<!DOCTYPE html>
<html lang="en">
<head>
<meta charset="utf-8">
<title>BrightTier – Data Analytics &amp; Professional Services</title>
<link href="https://fonts.googleapis.com/css2?family=Poppins:wght@300;400;500;600;700&family=Righteous&display=swap" rel="stylesheet">
<style>
:root{
  --magenta:#c21bbd;
  --magenta-soft:#e04fd8;
  --purple:#8a12e8;
  --pink:#f0319d;
  --teal:#0a7596;
  --bg:#0b0b2e;
  --bg-alt:#121240;
  --surface:#17174a;
  --surface-2:#1d1d55;
  --text:#ececf8;
  --muted:#a9aac8;
  --line:#a23ad8;
  --field:#ffffff;
  --field-text:#8a8aa0;
}
*{box-sizing:border-box;margin:0;padding:0}
html,body{width:1200px;height:3693px;overflow:hidden}
body{position:relative;background:var(--bg);font-family:"Poppins",sans-serif;color:var(--text)}
.abs{position:absolute}
.heading{font-family:"Righteous",sans-serif;font-weight:400}
.accent-bar{position:absolute;height:4px;width:34px;border-radius:2px;background:var(--magenta)}

/* header */
.brand{left:100px;top:16px;font-size:26px;font-weight:600;color:var(--magenta-soft);letter-spacing:.5px}
.signup{left:1005px;top:3px;width:116px;height:40px;border-radius:0 14px 14px 14px;background:var(--teal);color:#fff;font-size:13px;font-weight:600;display:flex;align-items:center;justify-content:center}

/* hero */
.hero-title{left:108px;top:146px;font-size:51px;line-height:54px;color:var(--text)}
.hero-text{left:108px;top:262px;width:380px;font-size:14px;line-height:25px;color:var(--muted)}
.btn-primary{display:flex;align-items:center;justify-content:center;color:#fff;font-size:13px;font-weight:600;letter-spacing:.3px;background:var(--magenta);border-radius:0 14px 0 14px}
.hero-btn{left:108px;top:330px;width:153px;height:43px}
.hero-visual{left:674px;top:79px;width:480px;height:430px;border-radius:40px 0 0 0;background:linear-gradient(135deg,#1e3ee0 0%,#4a6fae 45%,#6f8db4 70%,#173bd6 100%)}
.hero-rule{left:0;top:508px;width:1200px;height:1px;background:#20205a}

/* services */
.section-title{left:0;width:1200px;text-align:center;font-size:40px;color:var(--magenta-soft)}
.tab{top:681px;width:248px;height:49px;display:flex;align-items:center;justify-content:center;font-size:15px;font-weight:600;border-radius:0 16px 0 16px}
.tab-outline{left:337px;border:2px solid var(--line);color:var(--text)}
.tab-filled{left:614px;background:var(--teal);color:#fff}
.card{width:214px;height:198px;border:2px solid var(--line);border-radius:0 22px 0 22px;padding:28px 20px 0 20px;background:var(--surface)}
.card svg{width:40px;height:40px;display:block}
.card h3{margin-top:16px;font-size:14px;font-weight:600;color:var(--text)}
.card p{margin-top:10px;font-size:12.5px;line-height:20px;color:var(--muted)}

/* about */
.about{left:0;top:1283px;width:1200px;height:619px;background:var(--bg-alt)}
.about-visual{left:184px;top:1369px;width:372px;height:403px;border-radius:0 50px 0 50px;background:linear-gradient(150deg,#5d5f66 0%,#9aa3ad 35%,#3e5878 65%,#d6dde4 100%)}
.badge-dark{left:128px;top:1417px;width:190px;height:86px;border-radius:0 18px 0 18px;background:var(--teal);color:#fff;padding:26px 0 0 34px}
.badge-dark b{display:block;font-size:13px;font-weight:600}
.badge-dark span{font-size:12.5px}
.stat{background:var(--surface-2);border-radius:0 18px 0 18px;box-shadow:0 8px 22px rgba(0,0,0,.35);text-align:center}
.stat b{display:block;font-family:"Righteous",sans-serif;font-weight:400;font-size:38px;line-height:40px;color:var(--text)}
.stat span{font-size:12.5px;color:var(--muted)}
.stat-a{left:463px;top:1434px;width:164px;height:97px;padding-top:20px}
.stat-b{left:373px;top:1725px;width:162px;height:96px;padding-top:18px}
.ring{width:24px;height:24px;border-radius:50%;border:2px solid var(--magenta);display:flex;align-items:center;justify-content:center}
.ring::after{content:"";width:10px;height:10px;border-radius:50%;background:var(--magenta)}
.ring-soft{opacity:.55}
.about-title{left:640px;top:1384px;font-size:40px;color:var(--magenta-soft)}
.about-text{left:640px;top:1444px;width:430px;font-size:13px;line-height:20.5px;color:var(--muted)}
.bullet{left:640px;width:430px;font-size:13px;line-height:20.5px;color:var(--muted);padding-left:35px}
.bullet::before{content:"";position:absolute;left:0;top:9px;width:20px;height:3px;background:var(--magenta);border-radius:2px}
.btn-dark{display:flex;align-items:center;justify-content:center;color:#fff;font-size:13px;font-weight:600;background:var(--teal);border-radius:0 16px 0 16px}
.about-btn{left:640px;top:1718px;width:153px;height:43px}

/* newsletter */
.newsletter{left:140px;top:1986px;width:918px;height:331px;border-radius:0 86px 0 86px;background:linear-gradient(90deg,#8a1ee6 0%,#c52cc6 50%,#f0359f 100%);color:#fff;text-align:center}
.newsletter .kicker{position:absolute;left:0;top:80px;width:100%;font-size:12px}
.newsletter h2{position:absolute;left:0;top:104px;width:100%;font-size:37px;font-weight:600;font-family:"Poppins",sans-serif}
.subscribe{position:absolute;left:230px;top:169px;width:459px;height:40px;display:flex;border-radius:0 18px 0 18px;overflow:hidden;background:var(--field)}
.subscribe .field{flex:1;text-align:left;padding:10px 0 0 26px;font-size:12.5px;color:var(--field-text)}
.subscribe .go{width:148px;background:var(--bg);display:flex;align-items:center;justify-content:center;font-size:13px;font-weight:600;color:#fff}
.newsletter .note{position:absolute;left:0;top:233px;width:100%;font-size:12.5px}

/* testimonial */
.testimonial{left:0;top:2403px;width:1200px;height:650px;background:var(--bg-alt)}
.testi-text{left:295px;top:2552px;width:610px;text-align:center;font-size:13px;line-height:21px;color:var(--muted)}
.avatar{border-radius:50%;background:linear-gradient(160deg,#c9ced6,#6b7586)}
.quote-box{left:317px;top:2765px;width:565px;height:132px;border-radius:40px 0 40px 0;background:var(--teal);color:#e4ecf6;text-align:center;font-size:12.5px;line-height:21px;padding:27px 26px 0}
.quote-mark{left:572px;top:2754px;font-family:Georgia,serif;font-size:80px;color:rgba(255,255,255,.15);line-height:1}
.person{left:500px;top:2931px;width:200px;text-align:center}
.person b{display:block;font-size:14px;font-weight:600;color:var(--text)}
.person span{font-size:12px;color:var(--muted)}
.arrow{width:28px;height:28px;border-radius:50%;display:flex;align-items:center;justify-content:center}
.arrow-prev{left:488px;top:2937px;border:2px solid var(--magenta)}
.arrow-next{left:692px;top:2937px;background:var(--teal)}

/* contact */
.contact{left:0;top:3053px;width:1200px;height:592px;background:linear-gradient(90deg,#7c12e6 0%,#c126c9 50%,#ee2ea0 100%)}
.contact-title{left:0;top:3140px;width:1200px;text-align:center;color:#fff;font-size:37px;font-weight:600}
.contact-sub{left:0;top:3202px;width:1200px;text-align:center;color:#fff;font-size:13px}
.form-panel{left:184px;top:3258px;width:415px;height:313px;border-radius:0 50px 0 50px;background:var(--bg)}
.input{background:var(--field);border-radius:0 10px 0 10px;font-size:12.5px;color:var(--field-text);padding:7px 0 0 20px}
.submit{left:211px;top:3488px;width:361px;height:41px;font-size:14px}
.info-label{left:642px;color:#fff;font-size:14px;font-weight:600}
.info-label::before{content:"";position:absolute;left:0;top:-5px;width:20px;height:3px;background:var(--bg);border-radius:2px}
.info-value{left:642px;width:210px;color:#fff;font-size:13px;line-height:22px;opacity:.9}
.footer{left:0;top:3645px;width:1200px;height:48px;background:var(--bg);color:var(--text);font-size:13px;display:flex;align-items:center;justify-content:center}
</style>
</head>
<body>

<!-- header -->
<div class="abs brand">BrightTier</div>
<div class="abs signup">SING UP</div>

<!-- hero -->
<h1 class="abs heading hero-title">Remaking the way<br>we make things</h1>
<p class="abs hero-text">An IT business enabler and partner. We aim to be the link between you and your technological goal.</p>
<div class="abs btn-primary hero-btn">GET STARTED</div>
<div class="abs hero-visual" role="img" aria-label="Smiling man wearing a VR headset in front of diagonal blue stripes"></div>
<div class="abs hero-rule"></div>

<!-- services -->
<div class="accent-bar" style="left:583px;top:594px"></div>
<h2 class="abs heading section-title" style="top:600px">Our Services</h2>
<div class="abs tab tab-outline">DATA ANALYTICS</div>
<div class="abs tab tab-filled">PROFESSIONAL SERVICES</div>

<div class="abs card" style="left:140px;top:773px">
  <svg viewBox="0 0 40 40" fill="none" stroke="#e04fd8" stroke-width="3"><circle cx="17" cy="17" r="13"/><path d="M27 27l10 10"/><path d="M11 22v-5M17 22v-9M23 22v-6"/></svg>
  <h3>Data Analytics</h3><p>Lorem ipsum dolor sit aet, consectetur adiscing elit, sed do.</p>
</div>
<div class="abs card" style="left:374px;top:773px">
  <svg viewBox="0 0 40 40" fill="none" stroke="#e04fd8" stroke-width="3"><path d="M5 16h8l16-9v26l-16-9H5z"/><path d="M10 24l3 10h5l-2-10"/><path d="M34 14v12"/></svg>
  <h3>Marketing Analysis</h3><p>Lorem ipsum dolor sit aet, consectetur adiscing elit, sed do.</p>
</div>
<div class="abs card" style="left:609px;top:773px">
  <svg viewBox="0 0 40 40" fill="none" stroke="#e04fd8" stroke-width="2.5"><rect x="3" y="4" width="34" height="9" rx="2"/><rect x="3" y="16" width="34" height="9" rx="2"/><rect x="3" y="28" width="34" height="9" rx="2"/><path d="M8 8.5h4M8 20.5h4M8 32.5h4M22 8.5h10M22 20.5h10M22 32.5h10"/></svg>
  <h3>Server Analysis</h3><p>Lorem ipsum dolor sit aet, consectetur adiscing elit, sed do.</p>
</div>
<div class="abs card" style="left:843px;top:773px">
  <svg viewBox="0 0 40 40"><circle cx="20" cy="22" r="14" fill="#e04fd8"/><rect x="18" y="2" width="4" height="7" fill="#e04fd8"/><circle cx="15" cy="20" r="3" fill="#17174a"/><circle cx="25" cy="20" r="3" fill="#17174a"/><rect x="14" y="27" width="12" height="3" rx="1.5" fill="#17174a"/></svg>
  <h3>Machine Learning</h3><p>Lorem ipsum dolor sit aet, consectetur adiscing elit, sed do.</p>
</div>
<div class="abs card" style="left:374px;top:994px">
  <svg viewBox="0 0 40 40" fill="none" stroke="#e04fd8" stroke-width="3"><path d="M3 20c5-8 11-11 17-11s12 3 17 11c-5 8-11 11-17 11S8 28 3 20z"/><circle cx="20" cy="20" r="5" fill="#e04fd8"/><path d="M20 1v4M6 6l3 3M34 6l-3 3M20 35v4"/></svg>
  <h3>Data Visualization</h3><p>Lorem ipsum dolor sit aet, consectetur adiscing elit, sed do.</p>
</div>
<div class="abs card" style="left:609px;top:994px">
  <svg viewBox="0 0 40 40" fill="none" stroke="#e04fd8" stroke-width="2.5"><path d="M3 16l8-7 7 5 8-8 7 4"/><path d="M30 5h5v5"/><path d="M3 26l7-5 8 6 5-3 6 5 8-5"/><path d="M12 28l6 6 6-5"/></svg>
  <h3>Business Intelligence</h3><p>Lorem ipsum dolor sit aet, consectetur adiscing elit, sed do.</p>
</div>

<!-- about -->
<div class="abs about"></div>
<div class="abs about-visual" role="img" aria-label="Team at a desk reviewing data dashboards on a laptop"></div>
<div class="abs badge-dark"><b>DATA ANALYTICS</b><span>Lorem ipsum dolor</span></div>
<div class="abs stat stat-a"><b>99+</b><span>Satisfied Customers</span></div>
<div class="abs stat stat-b"><b>300+</b><span>Project Completed</span></div>
<div class="abs ring" style="left:141px;top:1772px"></div>
<div class="abs ring ring-soft" style="left:1038px;top:1366px"></div>
<div class="accent-bar" style="left:640px;top:1380px"></div>
<h2 class="abs heading about-title">About Us</h2>
<p class="abs about-text">Lorem ipsum dolor sit amet, consectetur adipiscing elit, sed do eiusmod tempor incididunt ut labore et dolore magna aliqua. Ut enim ad minim veniam, quis nostrud exercitation ullamco laboris nisi ut aliquip ex ea commodo consequat. Duis aute irure dolor in reprehenderit in voluptate velit esse cillum dolore eu fugiat nulla pariatur. Excepteur sint occaecat cupidatat non proident, sunt in culpa qui officia deserunt mollit anim id est laborum.</p>
<p class="abs bullet" style="top:1606px">Lorem ipsum dolor sit amet, consectetur adipiscing elit, sed do eiusmod tempor</p>
<p class="abs bullet" style="top:1662px">Lorem ipsum dolor sit amet, consectetur adipiscing elit,</p>
<div class="abs btn-dark about-btn">GET STARTED</div>

<!-- newsletter -->
<div class="abs newsletter">
  <div class="kicker">Get Latest News From Us</div>
  <h2>Subscribe to Our Newsletter</h2>
  <div class="subscribe"><div class="field">Your Email</div><div class="go">SUBSCRIBE</div></div>
  <div class="note">We Won't Send Any Spams. Promise!</div>
</div>

<!-- testimonial -->
<div class="abs testimonial"></div>
<div class="accent-bar" style="left:583px;top:2487px"></div>
<h2 class="abs heading section-title" style="top:2493px">Client Testimonial</h2>
<p class="abs testi-text">Lorem ipsum dolor sit amet, consectetur adipiscing elit, sed do eiusmod tempor incididunt ut labore et dolore magna aliqua. Ut enim ad minim veniam.</p>
<div class="abs avatar" style="left:547px;top:2628px;width:106px;height:106px" role="img" aria-label="Featured client portrait"></div>
<div class="abs avatar" style="left:221px;top:2701px;width:48px;height:48px" role="img" aria-label="Client portrait"></div>
<div class="abs avatar" style="left:193px;top:2863px;width:36px;height:36px;background:linear-gradient(160deg,#3fb6d6,#1c7ea0)" role="img" aria-label="Client portrait"></div>
<div class="abs avatar" style="left:944px;top:2700px;width:40px;height:40px" role="img" aria-label="Client portrait"></div>
<div class="abs avatar" style="left:985px;top:2810px;width:50px;height:50px;background:linear-gradient(160deg,#f08a6e,#e0553f)" role="img" aria-label="Client portrait"></div>
<div class="abs avatar" style="left:941px;top:2926px;width:36px;height:36px;background:linear-gradient(160deg,#9fd7c9,#5aa89a)" role="img" aria-label="Client portrait"></div>
<div class="abs quote-box">Lorem ipsum dolor sit amet, consectetur adipiscing elit, sed do eiusmod tempor incididunt ut labore et dolore magna aliqua. Ut enim ad minim veniam, quis nostrud exercitation ullamco laboris nisi ut aliquip ex ea commodo.</div>
<div class="abs quote-mark">&ldquo;</div>
<div class="abs arrow arrow-prev"><svg width="14" height="14" viewBox="0 0 14 14" fill="none" stroke="#e04fd8" stroke-width="2"><path d="M12 7H2M6 3L2 7l4 4"/></svg></div>
<div class="abs person"><b>Elan Varga</b><span>Lorem ipsum</span></div>
<div class="abs arrow arrow-next"><svg width="14" height="14" viewBox="0 0 14 14" fill="none" stroke="#fff" stroke-width="2"><path d="M2 7h10M8 3l4 4-4 4"/></svg></div>

<!-- contact -->
<div class="abs contact"></div>
<div class="accent-bar" style="left:583px;top:3135px;background:#fff"></div>
<h2 class="abs contact-title">Get in Touch With Us</h2>
<p class="abs contact-sub">You are clicksaway from your technological future</p>
<div class="abs form-panel"></div>
<div class="abs input" style="left:211px;top:3304px;width:173px;height:33px">Name*</div>
<div class="abs input" style="left:399px;top:3304px;width:173px;height:33px">Email*</div>
<div class="abs input" style="left:211px;top:3354px;width:173px;height:33px">Phone Number*</div>
<div class="abs input" style="left:399px;top:3354px;width:173px;height:33px">Company Name</div>
<div class="abs input" style="left:211px;top:3403px;width:361px;height:67px">Your Message</div>
<div class="abs btn-primary submit">SUBMIT</div>

<div class="abs info-label" style="top:3306px">Address</div>
<div class="abs info-value" style="top:3335px">123, Lorem ipsum dolor sit aet, consectetur adiscing.</div>
<div class="abs info-label" style="top:3402px">Phone Number</div>
<div class="abs info-value" style="top:3432px">123 456 7890</div>
<div class="abs info-label" style="top:3478px">Email Address</div>
<div class="abs info-value" style="top:3507px">info@brighttier.com</div>

<div class="abs footer">© 2023 BrightTier Data Analytics. All Rights Reserved.</div>

</body>
</html>
```